Shiatsu in der Kindlichen Entwicklung
Zielgruppe
Frauen, Familien
Aufgabenstellung
Es sollte ein buntes, gemaltes (Buntstift) aber trotzedem elegantes und ansprechendes Desigen haben.
Ich stelle mir einen Flyer vor, der ein Cover hat und kombinierbare einzelnen Seiten, die man dazu stecken kann. Je nach Interesse meiner Kunden.
Jedes Thema hat eine eigene Seite: Shiatsu in der Schwangerschaft, Baby Shiatsu und Kinder Shiatsu, Shiatsu in der Schule, Shiatsu Kurse usw. die dem Flyer beigefügt werden können.
Ich begleite Famielien und Kinder von klein bis gross.
Es sollten drei Abschnitte sein:
1. Shiatsu in der Schwangerschaft
2. Baby Shiatsu
3. Shiatsu mit Kindern

```html
<!DOCTYPE html>
<html lang="de">
<head>
<meta charset="utf-8">
<title>Flyer-Set Shiatsu</title>
<link href="https://fonts.googleapis.com/css2?family=Varela+Round&family=Patrick+Hand&display=swap" rel="stylesheet">
<style>
  :root{
    --pink:#ecc6c6; --green:#b0e8b0; --blue:#b0dde8; --red:#be0e20;
    --gold:#b8913a; --gold-light:#e9dca6; --ink:#1a1a1a; --white:#fff;
  }
  *{box-sizing:border-box;margin:0;padding:0}
  html,body{width:848px;height:1200px;overflow:hidden;background:var(--white)}
  body{position:relative;font-family:"Varela Round",sans-serif;color:var(--ink)}
  .card{position:absolute;width:235px;height:505px;background:var(--white);overflow:hidden;
        box-shadow:4px 8px 12px rgba(0,0,0,.28)}
  .card__photo{position:absolute;left:0;top:84px;width:235px;height:130px}
  .card__art{position:absolute;inset:0;width:235px;height:505px}
  .cover__eyebrow{position:absolute;left:12px;top:15px;font-size:11px;letter-spacing:.3px}
  .cover__title{position:absolute;left:11px;top:26px;font-size:17px;letter-spacing:.2px;white-space:nowrap}
  .cover__sub{position:absolute;right:9px;top:49px;font-size:10.5px;letter-spacing:.3px}
  .cover--red .cover__eyebrow,.cover--red .cover__title,.cover--red .cover__sub{color:var(--white)}
  .logo{position:absolute;left:12px;top:252px;width:74px;text-align:center}
  .logo__dot{width:60px;height:60px;border-radius:50%;background:var(--red);margin:0 auto 4px}
  .logo__name{font-size:7.5px;color:var(--red)}
  .specs{position:absolute;left:92px;top:261px;font-size:7px;line-height:11.5px}
  .specs ul{list-style:none;margin-top:6px}
  .specs li{padding-left:7px;position:relative;line-height:11.5px}
  .specs li::before{content:"•";position:absolute;left:0}
  .specs .plain::before{content:""}
  .person{position:absolute;left:100px;top:433px;font-size:7px;line-height:9px}
  .person__name{position:absolute;left:100px;top:352px;font-size:11.5px}
  .person__cred{position:absolute;left:100px;top:370px;font-size:7px;line-height:9px}
  .topic__title{position:absolute;left:0;right:0;text-align:center;font-family:"Patrick Hand",cursive;
        font-size:23px;line-height:25px;top:6px}
  .topic__title--single{top:18px}
  .topic__bird{position:absolute;width:40px;height:22px;border-radius:50% 50% 45% 45%;opacity:.85}
  .topic__text{position:absolute;left:13px;width:212px;font-size:7.4px;line-height:9.5px}
  .topic__text p+p{margin-top:9px}
  .topic__bar{position:absolute;left:0;width:235px;top:367px;height:14px;padding-left:13px;font-size:10px;line-height:14px}
  .topic__list{position:absolute;left:13px;top:386px;width:215px;list-style:none;font-size:7.4px;line-height:9.5px}
  .topic__list li{padding-left:6px;position:relative}
  .topic__list li::before{content:"";position:absolute;left:0;top:3.5px;width:3px;height:3px;border-radius:50%;background:var(--dot)}
  .topic--pink{--dot:var(--blue)} .topic--pink .topic__bar{background:linear-gradient(90deg,#f3d9dc,#fff)}
  .topic--blue{--dot:var(--pink)} .topic--blue .topic__bar{background:linear-gradient(90deg,#bfe3ec,#fff)}
  .topic--green{--dot:var(--green)} .topic--green .topic__bar{background:linear-gradient(90deg,#c4efc4,#fff)}
</style>
</head>
<body>

<!-- Cover, rosé -->
<section class="card cover" style="left:171px;top:83px">
  <div class="card__photo" role="img" aria-label="Foto: Gesichtsbehandlung mit Händen auf der Stirn" style="background:linear-gradient(135deg,#f3dccb,#d9a98c 60%,#efd3c0)"></div>
  <svg class="card__art" viewBox="0 0 235 505" aria-hidden="true">
    <path d="M0 0H235V68C160 58 80 56 0 64Z" fill="var(--pink)"/>
    <path d="M0 64C80 56 160 58 235 68V76C160 68 80 66 0 74Z" fill="var(--green)"/>
    <path d="M0 74C80 66 160 68 235 76V82C160 74 80 72 0 82Z" fill="var(--white)"/>
    <path d="M0 82C80 72 160 74 235 82V92C160 84 80 82 0 92Z" fill="var(--blue)"/>
    <path d="M0 212C70 202 150 196 235 201V505H0Z" fill="var(--white)"/>
    <path d="M0 207C70 198 150 192 235 197V207C150 203 70 210 0 218Z" fill="var(--blue)"/>
    <path d="M0 220C70 212 150 205 235 208V217C150 215 70 222 0 231Z" fill="var(--green)"/>
    <path d="M0 233C70 225 150 218 235 220V225C150 225 70 232 0 240Z" fill="var(--pink)"/>
    <path d="M0 482C60 474 110 484 160 474C195 467 218 466 235 470V505H0Z" fill="var(--pink)"/>
  </svg>
  <div class="cover__eyebrow">PRAXIS FÜR</div>
  <div class="cover__title">FERNÖSTLICHE MEDIZN</div>
  <div class="cover__sub">TCM &amp; SHIATSU</div>
  <div class="logo"><div class="logo__dot"></div><div class="logo__name">Praxis Hausner</div></div>
  <div class="specs">Spezialisiert auf:
    <ul><li>Shiatsu in der Schwangerschaft</li><li>Shiatsu mit Babys und Kindern</li><li>Schmerzen im Bewegungsapparat</li><li class="plain" style="line-height:8px">Menschen in seelischen Krisen</li></ul>
  </div>
  <div class="person__name">Mirela Hausner</div>
  <div class="person__cred">Dipl. Shiatsu-Therapeutin<br>velani Baby und<br>Kinder Shiatsu Therapeutin<br>Dorn Therapeutin</div>
  <div class="person" style="top:424px">Lindenweg 7<br>6312 Halden<br>Tel. 079 512 46 80<br>tcm-shiatsu-hausner.ch</div>
</section>

<!-- Cover, rot -->
<section class="card cover cover--red" style="left:426px;top:83px">
  <div class="card__photo" role="img" aria-label="Foto: Gesichtsbehandlung mit Händen auf der Stirn" style="background:linear-gradient(135deg,#f3dccb,#d9a98c 60%,#efd3c0)"></div>
  <svg class="card__art" viewBox="0 0 235 505" aria-hidden="true">
    <path d="M0 0H235V68C160 58 80 56 0 64Z" fill="var(--red)"/>
    <path d="M0 64C80 56 160 58 235 68V76C160 68 80 66 0 74Z" fill="var(--gold-light)"/>
    <path d="M0 74C80 66 160 68 235 76V82C160 74 80 72 0 82Z" fill="var(--white)"/>
    <path d="M0 82C80 72 160 74 235 82V92C160 84 80 82 0 92Z" fill="var(--gold)"/>
    <path d="M0 212C70 202 150 196 235 201V505H0Z" fill="var(--white)"/>
    <path d="M0 207C70 198 150 192 235 197V207C150 203 70 210 0 218Z" fill="var(--gold)"/>
    <path d="M0 220C70 212 150 205 235 208V217C150 215 70 222 0 231Z" fill="var(--gold-light)"/>
    <path d="M0 233C70 225 150 218 235 220V225C150 225 70 232 0 240Z" fill="var(--red)"/>
    <path d="M0 482C60 474 110 484 160 474C195 467 218 466 235 470V505H0Z" fill="var(--red)"/>
  </svg>
  <div class="cover__eyebrow">PRAXIS FÜR</div>
  <div class="cover__title">FERNÖSTLICHE MEDIZN</div>
  <div class="cover__sub">TCM &amp; SHIATSU</div>
  <div class="logo"><div class="logo__dot"></div><div class="logo__name">Praxis Hausner</div></div>
  <div class="specs">Spezialisiert auf:
    <ul><li>Shiatsu in der Schwangerschaft</li><li>Shiatsu mit Babys und Kindern</li><li>Schmerzen im Bewegungsapparat</li><li class="plain" style="line-height:8px">Menschen in seelischen Krisen</li></ul>
  </div>
  <div class="person__name">Mirela Hausner</div>
  <div class="person__cred">Dipl. Shiatsu-Therapeutin<br>velani Baby und<br>Kinder Shiatsu Therapeutin<br>Dorn Therapeutin</div>
  <div class="person" style="top:424px">Lindenweg 7<br>6312 Halden<br>Tel. 079 512 46 80<br>tcm-shiatsu-hausner.ch</div>
</section>

<!-- Einlage: Schwangerschaft -->
<section class="card topic topic--pink" style="left:49px;top:658px">
  <div class="card__photo" role="img" aria-label="Foto: Hände auf dem Bauch einer Schwangeren" style="background:linear-gradient(135deg,#fbeee6,#e9bfa6 55%,#f6e6dc)"></div>
  <svg class="card__art" viewBox="0 0 235 505" aria-hidden="true">
    <path d="M0 0H235V68C160 58 80 56 0 64Z" fill="var(--pink)"/>
    <path d="M0 64C80 56 160 58 235 68V76C160 68 80 66 0 74Z" fill="var(--green)"/>
    <path d="M0 74C80 66 160 68 235 76V82C160 74 80 72 0 82Z" fill="var(--white)"/>
    <path d="M0 82C80 72 160 74 235 82V92C160 84 80 82 0 92Z" fill="var(--blue)"/>
    <path d="M0 212C70 202 150 196 235 201V505H0Z" fill="var(--white)"/>
    <path d="M0 207C70 198 150 192 235 197V207C150 203 70 210 0 218Z" fill="var(--blue)"/>
    <path d="M0 220C70 212 150 205 235 208V217C150 215 70 222 0 231Z" fill="var(--green)"/>
    <path d="M0 233C70 225 150 218 235 220V225C150 225 70 232 0 240Z" fill="var(--pink)"/>
    <path d="M0 482C60 474 110 484 160 474C195 467 218 466 235 470V505H0Z" fill="var(--pink)"/>
  </svg>
  <h2 class="topic__title">Shiatsu in der<br>Schwangerschaft</h2>
  <div class="topic__bird" role="img" aria-label="Illustration: Vogel" style="left:80px;top:245px;background:linear-gradient(90deg,var(--pink),var(--green))"></div>
  <div class="topic__text" style="top:279px"><p>Wussten Sie, dass Shiatsu eine wunderbare Methode ist während der Schwangerschaft? Es wirkt unter­stützend, begleitend, geburtsvorbereitend und sehr entspannend. Diese Ruhe gibt den nötigen Raum, den oftmals kräfteraubenden Alltag auszublenden und wieder in den eigenen Körper zu lauschen. Dabei findet eine natürliche und innige Verbindung mit dem Baby statt. Das ist kraftspendend und harmonisierend.</p></div>
  <div class="topic__bar">Anwendungsgebiete</div>
  <ul class="topic__list"><li>Morgendlicher Übelkeit</li><li>Rückenschmerzen</li><li>Wassereinlagerungen</li><li>Schlafprobleme</li><li>Freude</li><li>Sorge</li><li>Ängste</li><li>Erfahrungen vorangegangener Geburten</li><li>Partnerübungen für alle Phasen der Geburt</li></ul>
</section>

<!-- Einlage: Baby -->
<section class="card topic topic--blue" style="left:304px;top:658px">
  <div class="card__photo" role="img" aria-label="Foto: Hände auf der Brust eines Babys" style="background:linear-gradient(135deg,#f6ebe6,#efcdbb 55%,#f4f0ee)"></div>
  <svg class="card__art" viewBox="0 0 235 505" aria-hidden="true">
    <path d="M0 0H235V68C160 58 80 56 0 64Z" fill="var(--blue)"/>
    <path d="M0 64C80 56 160 58 235 68V76C160 68 80 66 0 74Z" fill="var(--pink)"/>
    <path d="M0 74C80 66 160 68 235 76V82C160 74 80 72 0 82Z" fill="var(--white)"/>
    <path d="M0 82C80 72 160 74 235 82V92C160 84 80 82 0 92Z" fill="var(--green)"/>
    <path d="M0 212C70 202 150 196 235 201V505H0Z" fill="var(--white)"/>
    <path d="M0 207C70 198 150 192 235 197V207C150 203 70 210 0 218Z" fill="var(--blue)"/>
    <path d="M0 220C70 212 150 205 235 208V217C150 215 70 222 0 231Z" fill="var(--green)"/>
    <path d="M0 233C70 225 150 218 235 220V225C150 225 70 232 0 240Z" fill="var(--pink)"/>
    <path d="M0 482C60 474 110 484 160 474C195 467 218 466 235 470V505H0Z" fill="var(--blue)"/>
  </svg>
  <h2 class="topic__title topic__title--single">velani•Baby Shiatsu®</h2>
  <div class="topic__bird" role="img" aria-label="Illustration: Vogel" style="left:28px;top:223px;background:linear-gradient(90deg,var(--pink),var(--green))"></div>
  <div class="topic__text" style="top:252px">
    <p>Auf diese angenehme und sanfte Behandlung sprechen gerade Babys mit ihren feinsinnigen Empfindungen besonders gut an. Speziell für sie wurde velani•Baby Shiatsu® entwickelt, dass ausdrücklich auf die Bedürfnisse und Wünsche der Kleinsten eingeht und sie in der Entwicklung fördert.</p>
    <p>Gerade die ersten 18 Monate im Leben des Kindes sind prägend für seine ganze Entwicklung. Durch die liebevolle und achtsame Berührung wird Geborgenheit gegeben und Vertrauen geschaffen.</p>
  </div>
  <div class="topic__bar">Vorzüge</div>
  <ul class="topic__list"><li>unterstützt die Entwicklung des Kindes</li><li>vertieft den Kontakt und stärkt die Bindung von Mutter und Baby</li><li>ist hilfreich bei Schlafstörungen, Blähungen, Zahnen</li><li>kann selbst erlernt und zuhause umgesetzt werden</li><li>richtet das Baby durch Streicheleinheiten auf</li><li>ist gut für die Haltung, Gesundheit und emotionale Stabilität</li><li>optimiert die Wahrnehmung</li></ul>
</section>

<!-- Einlage: Kinder -->
<section class="card topic topic--green" style="left:559px;top:658px">
  <div class="card__photo" role="img" aria-label="Foto: Rückenbehandlung bei einem Kind auf grünem Tuch" style="background:linear-gradient(135deg,#e9e4d6,#d7a98b 50%,#9fd0b0)"></div>
  <svg class="card__art" viewBox="0 0 235 505" aria-hidden="true">
    <path d="M0 0H235V68C160 58 80 56 0 64Z" fill="var(--green)"/>
    <path d="M0 64C80 56 160 58 235 68V76C160 68 80 66 0 74Z" fill="var(--pink)"/>
    <path d="M0 74C80 66 160 68 235 76V82C160 74 80 72 0 82Z" fill="var(--white)"/>
    <path d="M0 82C80 72 160 74 235 82V92C160 84 80 82 0 92Z" fill="var(--blue)"/>
    <path d="M0 212C70 202 150 196 235 201V505H0Z" fill="var(--white)"/>
    <path d="M0 207C70 198 150 192 235 197V207C150 203 70 210 0 218Z" fill="var(--blue)"/>
    <path d="M0 220C70 212 150 205 235 208V217C150 215 70 222 0 231Z" fill="var(--green)"/>
    <path d="M0 233C70 225 150 218 235 220V225C150 225 70 232 0 240Z" fill="var(--pink)"/>
    <path d="M0 482C60 474 110 484 160 474C195 467 218 466 235 470V505H0Z" fill="var(--green)"/>
  </svg>
  <h2 class="topic__title">Kodama Kinder<br>Shiatsu</h2>
  <div class="topic__bird" role="img" aria-label="Illustration: Vogel" style="left:80px;top:268px;width:60px;height:30px;background:linear-gradient(90deg,var(--pink),var(--green))"></div>
  <div class="topic__text" style="top:329px"><p>Kodama Programm ist ein Schulprogramm für Primarschüler und Kinder bis zum Alter von etwa zwölf Jahren. Es setzt sich zusammen aus der Behandlungssequenz Kodama-Shiatsu.</p></div>
  <div class="topic__bar">Ziele</div>
  <ul class="topic__list" style="width:222px"><li>die Gesundheit zu fördern</li><li>die Konzentrationsfähigkeit zu verbessern</li><li>eine gesunde Haltung zu unterstützen</li><li>das Klassenklima zu verbessern</li><li>die Selbstwirksamkeit zu verbessern</li><li>ist eine Einführung in die japanische Kultur und Sprache</li><li>und macht Alt und Jung riesen grossen Spass</li></ul>
</section>

</body>
</html>
```